Verin Court Nine Flash website

we need a website to cater to 2 aspect of the business. We have Verin court residence and verin court office. For the office, we will get their inquire and arrange a face to face meetup to show them the office area for rent. For the residence side, it will need to be like lodgly or staymira.com. we want to allow them to book online for the date they need. We have a total of 10 different room configurations starting at $70 per night and up depending on the size of the room. example of the design is https://pelvandale.com/

Target Market(s)

the website should have detail information on the layout, designs, and luxury of the building.

Industry/Entity Type

office and service appartment rental/lease

Coding

Coded - Design and coding required

Number of Pages Required

5+ page

Requirements
Must have
• a luxury perspective
Nice to have
• example https://pelvandale.com/

```html
<!DOCTYPE html>
<html lang="en">
<head>
<meta charset="utf-8">
<title>Verin Court Nine</title>
<link href="https://fonts.googleapis.com/css2?family=Cormorant+Garamond:wght@400;500;600&family=DM+Sans:wght@400;500;700&display=swap" rel="stylesheet">
<style>
:root{
  --gold:#D69E2E;
  --gold-dark:#B8841C;
  --cream:#FDEFD2;
  --ink:#1B1B1B;
  --muted:#555;
  --white:#fff;
  --footer:#171717;
  --line:#E6E0D4;
}
*{box-sizing:border-box;margin:0;padding:0}
html,body{width:1200px;height:4914px;overflow:hidden}
body{font-family:'DM Sans',sans-serif;color:var(--ink);background:var(--white);position:relative}
.serif{font-family:'Cormorant Garamond',serif}
.abs{position:absolute}
.eyebrow{font-family:'Cormorant Garamond',serif;color:var(--gold);font-size:21px}
.h2{font-family:'Cormorant Garamond',serif;font-weight:500;font-size:40px;line-height:1.3}
.body-text{font-size:12.5px;line-height:1.75;color:var(--muted)}
.btn{display:inline-flex;align-items:center;gap:18px;background:var(--gold);color:#fff;font-size:12px;border-radius:4px;padding:0 28px;height:42px}
.btn svg{width:22px;height:10px}
.photo{border-radius:2px}

/* header */
.site-header{top:0;left:0;width:1200px;height:96px}
.logo{left:125px;top:30px;display:flex;align-items:center;gap:8px;color:var(--gold);font-family:'Cormorant Garamond',serif;font-size:15px}
.logo i{width:14px;height:14px;border:1.5px solid var(--gold)}
.nav{left:308px;top:44px;display:flex;gap:34px;font-size:13px}
.nav a{color:var(--ink);text-decoration:none}
.nav a.active{color:var(--ink);border-bottom:2px solid var(--gold);padding-bottom:6px}
.contact-btn{left:903px;top:34px;height:44px;width:170px;justify-content:center}

/* hero */
.hero-text{left:125px;top:200px;width:420px}
.hero-text h1{font-family:'Cormorant Garamond',serif;font-weight:500;font-size:54px;line-height:1.28;margin-top:12px}
.hero-text p{margin-top:16px;width:300px}
.hero-count{left:125px;top:538px;display:flex;align-items:center;gap:14px;font-size:20px;font-weight:700}
.hero-count span.bar{width:210px;height:1px;background:#333}
.circle-btn{width:32px;height:32px;border-radius:50%;border:1px solid #444;display:flex;align-items:center;justify-content:center}
.circle-btn svg{width:12px;height:12px}
.hero-arrows{left:398px;top:535px;display:flex;gap:10px}
.hero-card{top:150px;height:480px;border-radius:14px;overflow:hidden;color:#fff}
.hero-card .label{position:absolute;bottom:34px;left:22px;font-family:'Cormorant Garamond',serif;font-size:22px}
.hero-card .count{position:absolute;bottom:24px;right:26px;text-align:center;font-family:'Cormorant Garamond',serif;font-size:30px;line-height:1}
.hero-card .count small{display:block;font-size:12px}
.hero-card .vlabel{position:absolute;bottom:40px;left:18px;writing-mode:vertical-rl;transform:rotate(180deg);font-family:'Cormorant Garamond',serif;font-size:22px}

/* search */
.search{left:158px;top:633px;width:917px;height:123px;background:var(--cream);border-radius:6px}
.tabs{position:absolute;left:0;top:0;display:flex}
.tabs span{font-size:10px;padding:8px 14px;background:#F3DFB6;color:#333}
.tabs span.on{background:var(--gold);color:#fff}
.fields{position:absolute;left:0;top:48px;display:flex;gap:18px;padding:0 0}
.field{height:44px;background:#fff;border-radius:4px;display:flex;align-items:center;justify-content:space-between;padding:0 16px;font-size:11px;color:#555}
.field.adv{background:var(--gold);color:#fff;justify-content:center}

/* about */
.about-text{left:692px;top:850px;width:370px}
.about-text .h2{margin:6px 0 18px;font-size:38px}

/* welcome */
.welcome{top:1361px;left:0;width:1200px;height:945px;background:var(--cream)}
.center-head{position:absolute;left:0;width:1200px;text-align:center}
.center-head p.body-text{width:480px;margin:14px auto 0}
.prop-card{position:absolute;width:290px;background:#fff;border-radius:4px;padding:14px 14px 20px;text-align:center}
.prop-card .ph{height:166px}
.prop-card h3{font-family:'Cormorant Garamond',serif;font-weight:500;font-size:21px;margin-top:26px}
.price{color:var(--gold);font-weight:700;font-size:15px;margin-top:8px}
.per{font-size:12px;font-weight:700;margin-top:8px}
.addr{font-size:11px;margin-top:12px}
.amen{display:flex;justify-content:center;gap:24px;margin-top:14px;font-size:11px}
.amen span{display:flex;gap:6px;align-items:center}
.amen svg{width:16px;height:14px}
.side-arrow{position:absolute;width:28px;height:36px;background:var(--gold);border-radius:3px;display:flex;align-items:center;justify-content:center}

/* office */
.office-card{position:absolute;width:300px;text-align:center}
.office-card .ph{height:187px}
.office-card h3{font-family:'Cormorant Garamond',serif;font-weight:500;font-size:21px;margin-top:36px}
.dots{left:515px;top:3062px;display:flex;gap:22px}
.dots i{width:8px;height:8px;border-radius:50%;background:#999}
.dots i.on{background:var(--gold)}

/* testimonials */
.testi{top:3172px;left:0;width:1200px;height:612px;background:var(--cream)}
.t-card{position:absolute;top:314px;height:205px;background:#fff;padding:50px 60px 0}
.quote{position:absolute;right:50px;top:-32px;color:var(--gold);font-family:'Cormorant Garamond',serif;font-size:110px;line-height:1;font-weight:600}
.t-name{position:absolute;right:32px;bottom:48px;color:var(--gold);font-size:10px;letter-spacing:3px;font-weight:700}
.avatar{position:absolute;left:60px;bottom:-30px;width:78px;height:78px;border-radius:50%}

/* footer */
.footer{top:4353px;left:0;width:1200px;height:561px;background:var(--footer);color:#fff}
.footer h4{font-family:'Cormorant Garamond',serif;font-weight:500;font-size:24px}
.footer .col{position:absolute;top:228px;font-size:12px;line-height:1.95}
.vline{position:absolute;top:262px;width:1px;height:170px;background:#555}
.ci{display:flex;align-items:center;gap:16px;margin-top:20px;line-height:1.6}
.ci i{width:30px;height:30px;border-radius:50%;background:#fff;display:flex;align-items:center;justify-content:center;flex:none}
.ci svg{width:13px;height:13px}
</style>
</head>
<body>

<header class="abs site-header">
  <div class="abs logo"><i></i>Verin Court Nine</div>
  <nav class="abs nav">
    <a class="active">Home</a><a>About Us</a><a>Office Rentals</a><a>Home rentals</a><a>Blogs</a>
  </nav>
  <div class="abs btn contact-btn">Contact us <svg viewBox="0 0 22 10"><path d="M0 5h20M16 1l4 4-4 4" stroke="#fff" fill="none"/></svg></div>
</header>

<section>
  <div class="abs hero-text">
    <div class="eyebrow">Explore Rental Options</div>
    <h1>Houses and Offices for Every Need</h1>
    <p class="body-text">Lorem Ipsum is simply dummy text of the printing and typesetting industry.</p>
  </div>
  <div class="abs hero-count">01 <span class="bar"></span></div>
  <div class="abs hero-arrows">
    <div class="circle-btn"><svg viewBox="0 0 12 12"><path d="M4 2l4 4-4 4" stroke="#333" fill="none"/></svg></div>
    <div class="circle-btn"><svg viewBox="0 0 12 12"><path d="M8 2L4 6l4 4" stroke="#333" fill="none"/></svg></div>
  </div>
  <div class="abs hero-card" style="left:605px;width:310px;background:linear-gradient(180deg,#d9d8d2,#7f8a78 60%,#39423a)" role="img" aria-label="White villa with arched doorway and green shutters">
    <div class="label">Brand Homes</div>
    <div class="count">10<small>Rooms</small></div>
  </div>
  <div class="abs hero-card" style="left:930px;width:148px;background:linear-gradient(180deg,#c9cdd0,#7c7f7a 60%,#3b3d3a)" role="img" aria-label="Modern apartment tower">
    <div class="vlabel">Offices</div>
  </div>
  <div class="abs hero-card" style="left:1093px;width:130px;border-radius:14px 0 0 14px;background:linear-gradient(180deg,#bfc3c6,#6b625a 60%,#302c28)" role="img" aria-label="Residential building at dusk">
    <div class="vlabel">Homes</div>
  </div>

  <div class="abs search">
    <div class="tabs"><span>Buy</span><span>Per Room</span><span class="on">Sell</span></div>
    <div class="fields">
      <div class="field" style="width:256px;margin-left:0">Category <span>⌄</span></div>
      <div class="field" style="width:256px">Location <span>⌄</span></div>
      <div class="field adv" style="width:156px">Advanced</div>
      <div class="field" style="width:156px;justify-content:center">⌕&nbsp; Search Property</div>
    </div>
  </div>
</section>

<section>
  <div class="abs photo" style="left:125px;top:889px;width:222px;height:333px;background:linear-gradient(180deg,#e9ecee,#a8a9a4 55%,#5a5a54)" role="img" aria-label="White apartment block with balconies"></div>
  <div class="abs photo" style="left:367px;top:866px;width:244px;height:183px;background:linear-gradient(180deg,#d8d4cc,#8e8b84 70%,#4f4c47)" role="img" aria-label="Bright living room interior"></div>
  <div class="abs photo" style="left:367px;top:1070px;width:244px;height:186px;background:linear-gradient(180deg,#86b3dd,#556c85 60%,#2f3a48)" role="img" aria-label="Apartment building with blue balconies"></div>
  <div class="abs about-text">
    <div class="eyebrow">Every Time</div>
    <div class="h2">Your Partner in Finding the Perfect Space,</div>
    <p class="body-text">Lorem Ipsum is simply dummy text of the printing and typesetting industry. Lorem Ipsum has been the industry's standard dummy text ever since the 1500s, when an unknown printer took a galley of type and scrambled it to make a type specimen book.</p>
    <div class="btn" style="margin-top:24px">Read More <svg viewBox="0 0 22 10"><path d="M0 5h20M16 1l4 4-4 4" stroke="#fff" fill="none"/></svg></div>
  </div>
</section>

<section class="abs welcome">
  <div class="center-head" style="top:96px">
    <div class="eyebrow">Welcome Home</div>
    <div class="h2" style="margin-top:6px">Discover Your Ideal<br>Sanctuary Today.</div>
    <p class="body-text">Lorem Ipsum is simply dummy text of the printing and typesetting industry.</p>
  </div>
  <div class="side-arrow" style="left:96px;top:510px"><svg width="12" height="10" viewBox="0 0 12 10"><path d="M11 5H1M4 1L0 5l4 4" stroke="#fff" fill="none"/></svg></div>
  <div class="side-arrow" style="left:1075px;top:510px"><svg width="12" height="10" viewBox="0 0 12 10"><path d="M1 5h10M8 1l4 4-4 4" stroke="#fff" fill="none"/></svg></div>

  <div class="prop-card" style="left:125px;top:334px">
    <div class="ph" style="background:linear-gradient(180deg,#7fb6e6,#b9c8d4 60%,#6f7570)" role="img" aria-label="White residential tower against blue sky"></div>
    <h3>3 Bed Flat To Rent</h3><div class="price">£1,998 pcm</div><div class="per">Per Month</div><div class="addr">Aldren Row, Westmere W8</div>
    <div class="amen"><span><svg viewBox="0 0 16 14"><path d="M1 12V6h14v6M1 9h14M4 6V3h5v3" stroke="#D69E2E" fill="none"/></svg>1</span><span><svg viewBox="0 0 16 14"><path d="M1 7h14v3a3 3 0 01-3 3H4a3 3 0 01-3-3z" stroke="#D69E2E" fill="none"/></svg>3</span><span><svg viewBox="0 0 16 14"><rect x="1" y="3" width="14" height="9" stroke="#D69E2E" fill="none"/></svg>1</span></div>
  </div>
  <div class="prop-card" style="left:455px;top:334px">
    <div class="ph" style="background:linear-gradient(180deg,#5b8fd0,#8a6b4d 55%,#3f3a35)" role="img" aria-label="Brick and glass apartment building"></div>
    <h3>5 Bed Flat To Rent</h3><div class="price">£1,998 pcm</div><div class="per">Per Month</div><div class="addr">Aldren Row, Westmere W8</div>
    <div class="amen"><span><svg viewBox="0 0 16 14"><path d="M1 12V6h14v6M1 9h14M4 6V3h5v3" stroke="#D69E2E" fill="none"/></svg>3</span><span><svg viewBox="0 0 16 14"><path d="M1 7h14v3a3 3 0 01-3 3H4a3 3 0 01-3-3z" stroke="#D69E2E" fill="none"/></svg>5</span><span><svg viewBox="0 0 16 14"><rect x="1" y="3" width="14" height="9" stroke="#D69E2E" fill="none"/></svg>1</span></div>
  </div>
  <div class="prop-card" style="left:785px;top:334px">
    <div class="ph" style="background:linear-gradient(180deg,#9fc2e4,#6f7a82 55%,#343a40)" role="img" aria-label="City skyline with glass towers"></div>
    <h3>4 Bed Flat To Rent</h3><div class="price">£1,998 pcm</div><div class="per">Per Month</div><div class="addr">Aldren Row, Westmere W8</div>
    <div class="amen"><span><svg viewBox="0 0 16 14"><path d="M1 12V6h14v6M1 9h14M4 6V3h5v3" stroke="#D69E2E" fill="none"/></svg>2</span><span><svg viewBox="0 0 16 14"><path d="M1 7h14v3a3 3 0 01-3 3H4a3 3 0 01-3-3z" stroke="#D69E2E" fill="none"/></svg>4</span><span><svg viewBox="0 0 16 14"><rect x="1" y="3" width="14" height="9" stroke="#D69E2E" fill="none"/></svg>1</span></div>
  </div>
  <div class="btn" style="position:absolute;left:524px;top:800px;width:152px;justify-content:center">See All <svg viewBox="0 0 22 10"><path d="M0 5h20M16 1l4 4-4 4" stroke="#fff" fill="none"/></svg></div>
</section>

<section>
  <div class="center-head" style="top:2395px">
    <div class="eyebrow">Fuel Your Success</div>
    <div class="h2" style="margin-top:6px">Explore Our Range of<br>Office Rentals.</div>
    <p class="body-text">Lorem Ipsum is simply dummy text of the printing and typesetting industry.</p>
  </div>
  <div class="office-card" style="left:125px;top:2636px">
    <div class="ph" style="background:linear-gradient(180deg,#4b5560,#8d96a0 50%,#2f343a)" role="img" aria-label="Dark glass office towers"></div>
    <h3>3 Room Office To Rent</h3><div class="price">£1,998 pcm</div><div class="per">Per Month</div><div class="addr">Aldren Row, Westmere W8</div>
    <div class="amen"><span><svg viewBox="0 0 16 14"><path d="M1 12V6h14v6M1 9h14" stroke="#D69E2E" fill="none"/></svg>1</span><span><svg viewBox="0 0 16 14"><circle cx="8" cy="7" r="5" stroke="#D69E2E" fill="none"/></svg>3</span><span><svg viewBox="0 0 16 14"><rect x="1" y="3" width="14" height="9" stroke="#D69E2E" fill="none"/></svg>1</span></div>
  </div>
  <div class="office-card" style="left:448px;top:2636px">
    <div class="ph" style="background:linear-gradient(180deg,#a9cbe8,#6f8ea6 55%,#3d5163)" role="img" aria-label="Business district skyline"></div>
    <h3>6 Room Office To Rent</h3><div class="price">£3,998 pcm</div><div class="per">Per Month</div><div class="addr">Aldren Row, Westmere W8</div>
    <div class="amen"><span><svg viewBox="0 0 16 14"><path d="M1 12V6h14v6M1 9h14" stroke="#D69E2E" fill="none"/></svg>4</span><span><svg viewBox="0 0 16 14"><circle cx="8" cy="7" r="5" stroke="#D69E2E" fill="none"/></svg>6</span><span><svg viewBox="0 0 16 14"><rect x="1" y="3" width="14" height="9" stroke="#D69E2E" fill="none"/></svg>1</span></div>
  </div>
  <div class="office-card" style="left:773px;top:2636px">
    <div class="ph" style="background:linear-gradient(180deg,#5e6670,#9aa1a8 50%,#3a3f45)" role="img" aria-label="Tall glass office buildings"></div>
    <h3>4 Room Office To Rent</h3><div class="price">£2,998 pcm</div><div class="per">Per Month</div><div class="addr">Aldren Row, Westmere W8</div>
    <div class="amen"><span><svg viewBox="0 0 16 14"><path d="M1 12V6h14v6M1 9h14" stroke="#D69E2E" fill="none"/></svg>2</span><span><svg viewBox="0 0 16 14"><circle cx="8" cy="7" r="5" stroke="#D69E2E" fill="none"/></svg>4</span><span><svg viewBox="0 0 16 14"><rect x="1" y="3" width="14" height="9" stroke="#D69E2E" fill="none"/></svg>1</span></div>
  </div>
  <div class="abs dots"><i></i><i></i><i></i><i class="on"></i><i></i><i></i></div>
</section>

<section class="abs testi">
  <div class="abs" style="left:125px;top:92px">
    <div class="eyebrow">Our Testimonials</div>
    <div class="h2" style="margin-top:4px">See Why Our Renters<br>Love Us.</div>
  </div>
  <div class="abs circle-btn" style="left:955px;top:135px;width:50px;height:50px;border-color:#ccc;background:#fff"><svg viewBox="0 0 12 12"><path d="M8 2L4 6l4 4" stroke="#333" fill="none"/></svg></div>
  <div class="abs circle-btn" style="left:1027px;top:135px;width:50px;height:50px;border:none;background:var(--gold)"><svg viewBox="0 0 12 12"><path d="M4 2l4 4-4 4" stroke="#fff" fill="none"/></svg></div>
  <div class="t-card" style="left:125px;width:417px">
    <div class="quote">”</div>
    <p class="body-text" style="color:#333">It was popularised in the 1960s with the release of Letraset sheets containing Lorem Ipsum passages, and more recently with desktop publishing software.</p>
    <div class="t-name">MARA QUINLAN</div>
    <div class="avatar" style="background:linear-gradient(135deg,#c2452d,#5a2a1e)" role="img" aria-label="Customer portrait"></div>
  </div>
  <div class="t-card" style="left:650px;width:500px">
    <div class="quote">”</div>
    <p class="body-text" style="color:#333">It was popularised in the 1960s with the release of Letraset sheets containing Lorem Ipsum passages, and more recently with desktop publishing software.</p>
    <div class="t-name">MARA QUINLAN</div>
    <div class="avatar" style="background:linear-gradient(135deg,#f2b531,#2f4f7a)" role="img" aria-label="Customer portrait"></div>
  </div>
  <div class="t-card" style="left:1172px;width:40px;padding:0"></div>
</section>

<section>
  <div class="abs" style="left:125px;top:3886px;width:380px">
    <div class="eyebrow">Our Blogs</div>
    <div class="h2" style="margin:4px 0 14px">Your Guide to Rental<br>Success Starts Here.</div>
    <p class="body-text" style="width:330px">Lorem Ipsum is simply dummy text of the printing and typesetting industry. Lorem Ipsum has been the industry's standard dummy text ever since the 1500s, when an unknown printer took a galley of type and scrambled it to make a type specimen book.</p>
    <div class="btn" style="margin-top:24px;width:152px;justify-content:center">See All <svg viewBox="0 0 22 10"><path d="M0 5h20M16 1l4 4-4 4" stroke="#fff" fill="none"/></svg></div>
  </div>
  <div class="abs" style="left:542px;top:3922px;width:416px;height:295px;background:linear-gradient(135deg,#6d6a62,#3b4651 50%,#1e2226)" role="img" aria-label="Stacked shipping containers at a port">
    <div class="abs" style="left:44px;top:200px;color:#fff;font-size:12px">▦&nbsp;&nbsp; Aug 11, 2018</div>
    <div class="abs serif" style="left:44px;top:232px;color:#fff;font-size:16px;width:240px">Lorem Ipsum is simply dummy text of the</div>
  </div>
  <div class="abs" style="left:982px;top:3922px;width:218px;height:295px;background:linear-gradient(160deg,#c9d7e3,#a3313a 55%,#3b3b3b)" role="img" aria-label="Red truck on a highway"></div>
</section>

<footer class="abs footer">
  <div class="abs" style="left:0;top:92px;width:1200px;text-align:center">
    <div style="width:40px;height:40px;border:1.5px solid #fff;margin:0 auto 14px"></div>
    <div class="serif" style="font-size:19px;letter-spacing:1px">VERIN COURT NINE</div>
  </div>
  <div class="col" style="left:125px;width:230px">
    <h4>About Us</h4>
    <p style="margin-top:14px">Lorem Ipsum is simply dummy text of the printing and typesetting industry. Lorem Ipsum has been the industry's standard dummy text ever since the 1500s.</p>
  </div>
  <div class="vline" style="left:444px"></div>
  <div class="col" style="left:536px">
    <h4>Quick Links</h4>
    <div style="margin-top:14px">Home<br>About Us<br>Office Rental<br>Home rental<br>Our Blog<br>Contact Us</div>
  </div>
  <div class="vline" style="left:772px"></div>
  <div class="col" style="left:858px;width:260px">
    <h4>Contact Us</h4>
    <div class="ci"><i><svg viewBox="0 0 13 13"><path d="M3 1l2 3-1 1.5a7 7 0 003.5 3.5L9 8l3 2-1 2C6 12 1 7 1 2z" fill="#D69E2E"/></svg></i>555-204-7731</div>
    <div class="ci"><i><svg viewBox="0 0 13 13"><rect x="1" y="3" width="11" height="8" stroke="#D69E2E" fill="none"/><path d="M1 3l5.5 4L12 3" stroke="#D69E2E" fill="none"/></svg></i>hello@verincourtnine.com</div>
    <div class="ci"><i><svg viewBox="0 0 13 13"><path d="M6.5 12S2 7.5 2 5a4.5 4.5 0 019 0c0 2.5-4.5 7-4.5 7z" fill="#D69E2E"/><circle cx="6.5" cy="5" r="1.5" fill="#fff"/></svg></i>14 Marlow Lane,<br>Easton Hollow 4207</div>
  </div>
  <div class="abs" style="left:125px;top:493px;width:950px;height:1px;background:#444"></div>
  <div class="abs" style="left:200px;top:519px;font-size:10px">© Copyright 2024 <b>Verin Court</b> . All Rights Reserved</div>
  <div class="abs" style="left:912px;top:512px;width:28px;height:28px;border-radius:50%;background:#fff"></div>
  <div class="abs" style="left:958px;top:512px;width:28px;height:28px;border-radius:50%;background:#fff"></div>
</footer>

</body>
</html>
```